Ladies in Trade Global

We will be building the site using Dot Net Nuke content management system so design needs to be DNN compatible including fonts used.
Client has a site already www.ladiesintradeglobal.example
The overall look and feel desired by the client is for a professional yet social website. The website is to reflect the networking and professional training aspect of the clients business.
Pink and purple would be the dominant colours best used with white to maintain the clean professional feel.
Client likes www.galsofcommerce.example as an example
Images to use should be anything networking and awards type, I have attached their logo.
Homepage Layout
- Banner across the top with logo top left
- Horizontal navigation bar
- Newsletter sign up in the banner area
- Join facebook/twitter
- A large area for rotating images
- A side panel for upcoming events/training
- Room to put sponsors logo’s across bottom of page.
Content page Layout
- Will not need the large area for rotating images
- Join Facebook/Twitter
- Room for content
- Side Panel to out in newsletter signup and upcoming events
Sitemap
o Home
o About Us
o History
o Events
? -International Women’s Day
? - Guidance Medal
? - Skills and Careers Fair
? - Rosy Day
? - Networking Gallery
o Membership
? - Why Join?
? - Membership Form
o Training
? - Computer Training
? - Function Planning Academy
? - KQR Junior Scheme
o Latest News
? - Media Articles
? - Current Newsletter
? - Links
o Blog
o Contact Us
Hi everyone
Thanks you so much for submitting designs, I will be presenting them to my client on Monday so will let you know feedback after that.
Cheers
Tamsin
Hi designers
We gave the designs to our client before xmas but due to xmas/new year break they haven't responded as yet. We get back on 10th January so we sould have a respose from them by then.
Thanks for your patience.
Cheers
Tamsin
Hi everyone
Thanks for your patience we have had some major flooding in SE QLD so has closed a lot of businesses down until yesterday, we are hoping to meet with our client this week to select a design.
Cheers
Tamsin
Hi everyone
I appreciate your patience with this project.....I am still waiting on my client to make a decision on design am hoping it will be next week so I can close this project.
Cheers
Tamsin
Hi everyone
I've finally heard back from the client who have now been caught in Cyclone Omba.....but they have told me they will be selecting a design next Tuesday so I will let you know outcome asap.
Apologies for the delay with this project.
Thanks
Tamsin

```html
<!DOCTYPE html>
<html lang="en">
<head>
<meta charset="utf-8">
<title>Ladies in Trade Global</title>
<link href="https://fonts.googleapis.com/css2?family=Ubuntu:wght@400;500;700&display=swap" rel="stylesheet">
<style>
:root{
  --navy:#0e1530;
  --magenta:#c2007a;
  --pink:#c4106e;
  --ink:#1d1d1d;
  --blue:#2f3c7e;
  --blue-soft:#8a93bd;
  --nav-top:#43548f;
  --nav-bottom:#25326a;
  --nav-active:#141b36;
  --white:#ffffff;
  --rule:#c9cde0;
}
*{box-sizing:border-box;margin:0;padding:0}
html,body{width:1011px;height:1200px;overflow:hidden}
body{
  font-family:"Ubuntu",sans-serif;
  color:var(--ink);
  background:linear-gradient(to bottom,var(--navy) 0,var(--navy) 150px,var(--magenta) 300px,var(--magenta) 100%);
  position:relative;
}
.page{
  position:absolute;left:126px;top:22px;width:760px;height:1155px;
  background:var(--white);border-radius:7px;overflow:hidden;
  box-shadow:0 0 12px rgba(0,0,0,.35);
}
.abs{position:absolute}
/* header */
.brand{left:26px;top:40px;display:flex;align-items:center;gap:8px}
.brand-mark{width:34px;height:34px;border-radius:50%;background:#d8dcec}
.brand-name{font-size:17px;font-weight:700;color:var(--blue);line-height:1.1;width:110px}
.follow{left:538px;top:26px;font-size:11px;font-weight:700;color:var(--blue)}
.social{top:22px;width:21px;height:21px;border-radius:3px}
.social.one{left:686px;background:#38b6e8}
.social.two{left:716px;background:#3d5a98}
.subscribe-label{left:536px;top:76px;font-size:11.5px;font-weight:700;color:var(--blue)}
.email{left:536px;top:96px;width:147px;height:18px;border:1px solid #333;font-size:9.5px;padding:3px 6px;color:#333}
.submit{left:693px;top:96px;width:45px;height:18px;background:var(--pink);color:var(--white);font-size:9.5px;text-align:center;line-height:18px;border-radius:2px}
/* nav */
.nav{left:0;top:135px;width:760px;height:35px;display:flex;background:linear-gradient(var(--nav-top),var(--nav-bottom))}
.nav a{display:block;height:35px;line-height:36px;text-align:center;color:var(--white);font-size:11.5px;text-decoration:none;border-left:1px solid #5a6aa3;text-shadow:0 1px 1px rgba(0,0,0,.5)}
.nav a.active{background:var(--nav-active);border-top:3px solid var(--pink);line-height:31px;border-left:none}
/* hero */
.hero{left:0;top:170px;width:760px;height:264px;background:linear-gradient(90deg,#d9dcde 0%,#b9b4ac 35%,#e4e2dc 55%,#c9b59a 75%,#8a8a8f 100%)}
.pager{left:305px;top:416px;width:100px;height:27px;background:#e6e6e6;border-radius:0 0 6px 6px;display:flex;justify-content:center;align-items:center;gap:5px;box-shadow:0 1px 2px rgba(0,0,0,.3)}
.dot{width:12px;height:12px;border-radius:50%;background:#d0d0d0;border:1px solid #a9a9a9}
.dot.on{background:var(--pink);border-color:#8c0a52}
/* welcome */
h1.welcome{left:21px;top:470px;font-size:19.5px;font-weight:400;color:var(--pink)}
.copy{font-size:9.3px;line-height:11.4px}
.quote{left:21px;top:555px;width:400px;text-align:center;font-size:13.4px;color:var(--blue);line-height:17.5px}
.supporters{left:32px;top:626px;width:405px;list-style:none;font-size:9.3px;line-height:14.2px}
.supporters li{padding-left:13px;position:relative}
.supporters li::before{content:"";position:absolute;left:1px;top:4px;width:6px;height:6px;background:var(--pink);transform:rotate(45deg) scale(.8)}
.supporters span{color:var(--pink)}
.body-text{left:21px;top:816px;width:410px;font-size:9.3px;line-height:14.3px}
.signoff{font-weight:700}
/* events */
.events{left:457px;top:461px;width:281px;height:467px;border:2px solid #d6d9e6;border-radius:7px;box-shadow:0 0 4px rgba(0,0,0,.12)}
.events h2{position:absolute;left:19px;top:8px;font-size:19.5px;font-weight:400;color:var(--pink)}
.event{position:absolute;left:19px;width:249px}
.event h3{font-size:14px;font-weight:700;color:var(--blue)}
.event .date{font-size:9.5px;font-weight:700;color:var(--blue-soft);margin-top:4px}
.event p{font-size:9.1px;line-height:11.4px;text-align:justify;margin-top:2px}
.event .more{text-align:right;font-size:9.8px;font-weight:700;color:var(--blue);margin-top:1px}
.sep{position:absolute;left:8px;width:262px;height:1px;background:linear-gradient(90deg,transparent,#9aa2c6,transparent)}
/* sponsors */
.sponsors{left:0;top:1006px;width:760px;height:99px;border-top:2px solid #d6d9e6;display:flex;justify-content:space-around;align-items:center;padding:0 14px}
.sponsor{font-size:14px;font-weight:700;color:#111;text-align:center}
.sponsor.clinic{color:#c98a3c;font-size:10px;line-height:12px}
/* footer */
.footer{left:0;top:1105px;width:760px;height:50px;background:linear-gradient(var(--nav-top),var(--nav-bottom));color:var(--white)}
.footer-links{position:absolute;left:21px;top:18px;font-size:11px;text-shadow:0 1px 1px rgba(0,0,0,.5)}
.copyright{position:absolute;right:21px;top:19px;font-size:9.6px}
</style>
</head>
<body>
<div class="page">
  <div class="abs brand"><span class="brand-mark"></span><span class="brand-name">Ladies in Trade Global</span></div>
  <div class="abs follow">Follow us on:</div>
  <div class="abs social one" role="img" aria-label="Social network link"></div>
  <div class="abs social two" role="img" aria-label="Social network link"></div>
  <div class="abs subscribe-label">Subscribe to our Newsletter</div>
  <div class="abs email">Type your email address</div>
  <div class="abs submit">SUBMIT</div>

  <nav class="abs nav">
    <a class="active" style="width:70px">HOME</a>
    <a style="width:97px">ABOUT US</a>
    <a style="width:92px">HISTORY</a>
    <a style="width:88px">EVENTS</a>
    <a style="width:114px">MEMBERSHIP</a>
    <a style="width:117px">LATEST NEWS</a>
    <a style="width:72px">BLOG</a>
    <a style="width:110px">CONTACT US</a>
  </nav>

  <div class="abs hero" role="img" aria-label="Rotating photo of professional women networking in a bright office"></div>
  <div class="abs pager"><span class="dot on"></span><span class="dot"></span><span class="dot"></span><span class="dot"></span><span class="dot"></span></div>

  <h1 class="abs welcome">Welcome to Ladies in Trade Global</h1>
  <p class="abs copy" style="left:21px;top:509px;width:410px">Congratulations on connecting with the nation's premier training and networking organisation for women.<br>You're in good company! Ladies in Trade Global's philosophy is</p>
  <p class="abs quote">Women who make a difference<br>make all the difference for other women</p>
  <p class="abs copy" style="left:21px;top:606px">We have the support of high profile Australian women including:</p>
  <ul class="abs supporters">
    <li><span>Carla Bennet</span> Fashion Designer</li>
    <li><span>Priya Zammit</span> (Inaugural recipient of the International Women's Day Guidance Medal)</li>
    <li>Olympic swimming champion <span>Sally Rowe</span></li>
    <li>QLD Telvana Businesswoman of the Year<br><span>Marisa Monteith</span> (Queensland)</li>
    <li>former Miss World <span>Bianca Greer</span></li>
    <li>television celebrity <span>Helena Pierce</span></li>
    <li>etiquette guru <span>Joan Darcy-Wells</span></li>
    <li>Sunday Courier gossip columnist <span>Rhea Raines</span></li>
    <li>Honourable <span>Karen Sutton AM</span> (the Longest serving female parliamentarian in the history of the Australian Government)</li>
    <li><span>Ellie Snowden</span> (Inaugural recipient of the International Women's Day Youth Guidance Patron Medal)</li>
  </ul>
  <div class="abs body-text">
    <p>With their help - and the support of our 6000 members right around the country - Ladies in Trade Global is able to assist thousands of women to realise their dreams, maximise their business potential and have helped thousands of women return to meaningful work.<br>Through our leadership program, we also aim to encourage Australian women to participate in public life at a policy-making level. So read on!<br>You too can be a part of the most dynamic, visionary and innovative</p>
    <p style="margin-top:14.3px">I look forward to meeting you in the near future.</p>
    <p style="margin-top:14.3px">In friendship,</p>
    <p class="signoff">Jocelyn Tobin</p>
  </div>

  <aside class="abs events">
    <h2>Upcoming Events</h2>
    <div class="event" style="top:40px">
      <h3>Lorem ipsum dolor sit amet</h3>
      <div class="date">December 6th 2010</div>
      <p>Lorem ipsum dolor sit amet, consectetur adipiscing elit. Maecenas nec mauris tellus, at euismod eros. Nam vitae ipsum non lacus dignissim vulputate ac eu lorem. Vestibulum molestie ultricies iaculis. Sed elementum bibendum arcu ac aliquam. Mauris consectetur dictum diam et adipiscing.</p>
      <div class="more">Read more</div>
    </div>
    <div class="sep" style="top:169px"></div>
    <div class="event" style="top:185px">
      <h3>Lorem ipsum dolor sit amet</h3>
      <div class="date">December 6th 2010</div>
      <p>Lorem ipsum dolor sit amet, consectetur adipiscing elit. Maecenas nec mauris tellus, at euismod eros. Nam vitae ipsum non lacus dignissim vulputate ac eu lorem. Vestibulum molestie ultricies iaculis. Sed elementum bibendum arcu ac aliquam. Mauris consectetur dictum diam et adipiscing.</p>
      <div class="more">Read more</div>
    </div>
    <div class="sep" style="top:314px"></div>
    <div class="event" style="top:330px">
      <h3>Lorem ipsum dolor sit amet</h3>
      <div class="date">December 6th 2010</div>
      <p>Lorem ipsum dolor sit amet, consectetur adipiscing elit. Maecenas nec mauris tellus, at euismod eros. Nam vitae ipsum non lacus dignissim vulputate ac eu lorem. Vestibulum molestie ultricies iaculis. Sed elementum bibendum arcu ac aliquam. Mauris consectetur dictum diam et adipiscing.</p>
      <div class="more">Read more</div>
    </div>
  </aside>

  <div class="abs sponsors">
    <div class="sponsor">The Cooks Kitbox</div>
    <div class="sponsor clinic">The Willow Clinic<br>Cosmetic, plastic and laser surgery</div>
    <div class="sponsor">The Cooks Kitbox</div>
    <div class="sponsor clinic">The Willow Clinic<br>Cosmetic, plastic and laser surgery</div>
    <div class="sponsor">The Cooks Kitbox</div>
  </div>

  <footer class="abs footer">
    <div class="footer-links">HOME | ABOUT US | HISTORY | EVENTS | MEMBERSHIP | LATEST NEWS | BLOG | CONTACT US</div>
    <div class="copyright">Copyright © 2010 Ladies in Trade Global</div>
  </footer>
</div>
</body>
</html>
```